Business card for auto dealership

Looking for a clean modern design.
Would like attached logo incorporated

Industry/Entity Type

Car dealership

Contact Information for Business Card

Name, website, phone, cell, fax, email

```html
<!DOCTYPE html>
<html lang="en">
<head>
<meta charset="utf-8">
<title>Brenner Truck &amp; Auto Sales – Business Card</title>
<link rel="stylesheet" href="https://fonts.googleapis.com/css2?family=Open+Sans:wght@300;400;600&family=Marcellus&display=swap">
<style>
  :root {
    --page: #e4e4e4;
    --card-white: #ffffff;
    --card-black: #050505;
    --sheen-light: #d6d6d6;
    --sheen-mid: #8a8a8a;
    --ink: #0a0a0a;
    --text-light: #e8e8e8;
    --text-soft: #cfcfcf;
    --rule: #5a5a5a;
    --ghost: #161616;
  }
  * { margin: 0; padding: 0; box-sizing: border-box; }
  html, body { width: 1200px; height: 900px; overflow: hidden; background: var(--page); }
  .sheet { position: relative; width: 1200px; height: 900px; }
  .card {
    position: absolute; left: 240px; width: 720px; height: 411px;
    background: var(--card-white); overflow: hidden;
    box-shadow: 0 6px 18px rgba(0,0,0,0.18);
  }
  .card--front { top: 24px; }
  .card--back { top: 465px; }
  .card__shapes { position: absolute; inset: 0; width: 100%; height: 100%; }

  .brand {
    position: absolute; display: flex; align-items: center; gap: 12px;
    font-family: "Open Sans", sans-serif; font-weight: 600; color: var(--ink);
    white-space: nowrap;
  }
  .brand__mark { width: 14px; height: 14px; background: var(--ink); flex: none; }
  .brand__name { font-size: 30px; line-height: 1.15; }
  .brand__line { display: block; }
  .card--front .brand { left: 80px; top: 228px; }
  .card--back .brand { left: 400px; top: 52px; }
  .card--back .brand__name { font-size: 26px; }

  .ghost-name {
    position: absolute; left: 312px; top: 168px;
    font-family: "Open Sans", sans-serif; font-weight: 600; font-size: 80px;
    color: var(--ghost); white-space: nowrap;
    transform: translate(-50%, -50%) rotate(-108deg);
  }

  .contact { position: absolute; left: 40px; top: 150px; color: var(--text-light); font-family: "Open Sans", sans-serif; }
  .contact__name { font-family: "Marcellus", serif; font-size: 20px; letter-spacing: 1px; }
  .contact__role { font-family: "Marcellus", serif; font-size: 17px; color: var(--text-soft); }
  .contact__rule { width: 230px; height: 1px; background: var(--rule); margin: 10px 0 14px; }
  .contact__rule--wide { width: 300px; }
  .contact__list { list-style: none; font-size: 17px; font-weight: 300; line-height: 1.45; }
  .contact__list li { display: flex; align-items: center; gap: 10px; }
  .contact__list svg { width: 14px; height: 14px; flex: none; }
</style>
</head>
<body>
<main class="sheet">

  <section class="card card--front" aria-label="Card front">
    <svg class="card__shapes" viewBox="0 0 720 411" preserveAspectRatio="none">
      <defs>
        <linearGradient id="sheen" x1="0" y1="0" x2="1" y2="1">
          <stop offset="0" stop-color="var(--sheen-light)"/>
          <stop offset="0.6" stop-color="var(--sheen-mid)"/>
          <stop offset="1" stop-color="#1a1a1a"/>
        </linearGradient>
      </defs>
      <polygon points="326,0 554,0 684,411 488,411" fill="url(#sheen)"/>
      <polygon points="340,0 554,0 684,411 505,411" fill="var(--card-black)"/>
    </svg>
    <div class="brand">
      <span class="brand__mark"></span>
      <span class="brand__name"><span class="brand__line">Brenner</span><span class="brand__line">Truck &amp; Auto Sales</span></span>
    </div>
  </section>

  <section class="card card--back" aria-label="Card back">
    <svg class="card__shapes" viewBox="0 0 720 411" preserveAspectRatio="none">
      <defs>
        <linearGradient id="sheen-back" x1="0" y1="0" x2="1" y2="1">
          <stop offset="0" stop-color="#2a2a2a"/>
          <stop offset="0.6" stop-color="var(--sheen-mid)"/>
          <stop offset="1" stop-color="var(--sheen-light)"/>
        </linearGradient>
      </defs>
      <rect width="720" height="411" fill="var(--card-black)"/>
      <polygon points="302,0 720,0 720,411 428,411" fill="url(#sheen-back)"/>
      <polygon points="318,0 720,0 720,411 448,411" fill="var(--card-white)"/>
    </svg>
    <div class="ghost-name" aria-hidden="true">Brenner</div>
    <div class="brand">
      <span class="brand__mark"></span>
      <span class="brand__name"><span class="brand__line">Brenner</span><span class="brand__line">Truck &amp; Auto Sales</span></span>
    </div>

    <div class="contact">
      <p class="contact__name">DANIEL REYES</p>
      <p class="contact__role">Director</p>
      <div class="contact__rule"></div>
      <ul class="contact__list">
        <li><svg viewBox="0 0 14 14"><rect x="3.5" y="1" width="7" height="12" rx="1" fill="none" stroke="currentColor"/></svg>555-201-7410</li>
        <li><svg viewBox="0 0 14 14"><path d="M2 6 Q7 1 12 6 L11 7 L9 6 Q7 5 5 6 L3 7 Z M4 8 H10 L11 12 H3 Z" fill="currentColor"/></svg>555-201-7410</li>
        <li><svg viewBox="0 0 14 14"><rect x="2" y="6" width="10" height="6" fill="none" stroke="currentColor"/><rect x="4" y="2" width="6" height="4" fill="none" stroke="currentColor"/></svg>555-366-1200</li>
      </ul>
      <div class="contact__rule contact__rule--wide"></div>
      <ul class="contact__list">
        <li><svg viewBox="0 0 14 14"><rect x="1.5" y="3" width="11" height="8" fill="none" stroke="currentColor"/><path d="M1.5 3 L7 8 L12.5 3" fill="none" stroke="currentColor"/></svg>info@brennerauto.com</li>
        <li><svg viewBox="0 0 14 14"><circle cx="7" cy="7" r="5.5" fill="none" stroke="currentColor"/><path d="M1.5 7 H12.5 M7 1.5 Q4 7 7 12.5 Q10 7 7 1.5" fill="none" stroke="currentColor"/></svg>www.brennerauto.com</li>
      </ul>
    </div>
  </section>

</main>
</body>
</html>
```